High Profile Government Site Design

We need some concept designs for a website that will be used for reporting campaign contributions to politicians. I am including some images to give you an idea of what has been done so far. Basically the deliverable should be a landing page and perhaps a content page we can use to put in our charts and data tables. The landing page should be in a tiled format so we can list featured elections, show some general inforgraphical information, and offer a search capability. We do not want you to use the existing site design or logo in the images provided but to come up with your own concepts so we can share them with the committee that decides the final look. There is an existing site for this application located at http://apps.velmorstate.gov/apps/election/cfs/search/CandidateSearch.aspx . If you win there may be more work on this project and other projects.

Target Market(s)

Political

Industry/Entity Type

Government

Number of Pages Required

2 page

Font styles to use
Sans Serif

Colors

Designer to choose colors to be used in the design.

Requirements
Nice to have
• Some ideas are on the landing page offering up some segments for races of interest, contributors of interest, some statistical information, and potentially a search bar.
Should not have
• Should not use the current design or logo

```html
<!DOCTYPE html>
<html lang="en">
<head>
<meta charset="utf-8">
<title>Fund Lantern</title>
<link href="https://fonts.googleapis.com/css2?family=Figtree:wght@400;500;600;700;800&display=swap" rel="stylesheet">
<style>
  :root {
    --bg-deep: #2a1a6e;
    --bg-mid: #4a2f9a;
    --nav-dark: #15112e;
    --home: #d2601a;
    --green: #2e9a74;
    --orange: #c56a31;
    --red: #c94a55;
    --purple: #8e46b4;
    --slate: rgba(44, 56, 98, 0.88);
    --gold: #d09a2e;
    --blue: #3a8fd6;
    --btn-dark: #231563;
    --white: #ffffff;
    --muted: rgba(255,255,255,0.7);
  }
  * { box-sizing: border-box; margin: 0; padding: 0; }
  html, body { width: 1200px; height: 738px; overflow: hidden; }
  body {
    font-family: "Figtree", sans-serif;
    color: var(--white);
    position: relative;
    background: linear-gradient(160deg, var(--bg-mid) 0%, var(--bg-deep) 55%, #3b2b6e 100%);
  }
  .backdrop {
    position: absolute; inset: 0;
    background: radial-gradient(ellipse at 50% 75%, rgba(150,140,190,0.35), transparent 60%);
  }
  .brand {
    position: absolute; left: 75px; top: 28px;
    font-size: 31px; font-weight: 700; letter-spacing: 0.2px; white-space: nowrap;
  }
  .social {
    position: absolute; right: 74px; top: 38px;
    display: flex; gap: 12px; list-style: none;
    font-size: 11px; font-weight: 600; text-transform: uppercase; letter-spacing: 0.3px;
  }
  .nav { position: absolute; top: 88px; left: 0; height: 43px; width: 100%; }
  .nav a {
    position: absolute; top: 0; height: 43px;
    display: flex; align-items: center; justify-content: center;
    background: var(--nav-dark); color: var(--white); text-decoration: none;
    font-size: 13px; font-weight: 700; white-space: nowrap;
  }
  .nav a.active { background: var(--home); }
  .site-search {
    position: absolute; left: 857px; top: 88px; width: 269px; height: 43px;
    border: 1px solid rgba(255,255,255,0.6);
    display: flex; align-items: center; justify-content: space-between;
    padding: 0 14px 0 16px; font-size: 13px;
  }
  .tile { position: absolute; }
  .tile-title {
    position: absolute; font-size: 16px; font-weight: 700; text-transform: uppercase; letter-spacing: 0.3px; white-space: nowrap;
  }
  .photo { left: 75px; top: 148px; width: 346px; height: 183px;
    background: linear-gradient(135deg, #7d6f6a, #d9d5d2 45%, #b04a3f 100%); }
  .about { left: 434px; top: 148px; width: 213px; height: 183px; background: var(--green); }
  .about .icon-slot { position: absolute; left: 19px; top: 19px; width: 82px; height: 77px;
    background: rgba(255,255,255,0.85); border-radius: 38px 38px 10px 10px; }
  .services { left: 657px; top: 148px; width: 213px; height: 183px; background: var(--orange); }
  .election-search { left: 884px; top: 148px; width: 242px; height: 183px; background: var(--red); padding: 20px 14px; }
  .election-search h2 { font-size: 16px; font-weight: 700; margin-bottom: 14px; }
  .select {
    background: var(--white); color: #444; height: 34px; margin-bottom: 9px;
    display: flex; align-items: center; justify-content: space-between;
    padding: 0 12px; font-size: 13px;
  }
  .search-btn {
    position: absolute; right: 14px; bottom: 15px; width: 82px; height: 32px;
    background: var(--btn-dark); font-size: 12px; font-weight: 700;
    display: flex; align-items: center; justify-content: center;
  }
  .featured { left: 75px; top: 343px; width: 346px; height: 341px; background: var(--purple); padding: 22px 20px 0 17px; }
  .featured h2 { font-size: 16px; font-weight: 700; margin-bottom: 12px; }
  .featured ul { list-style: none; }
  .featured li {
    height: 39px; display: flex; align-items: center; gap: 14px; white-space: nowrap;
    font-size: 13px; font-weight: 500; letter-spacing: 0.2px; border-bottom: 1px solid rgba(255,255,255,0.28);
  }
  .featured li:last-child { border-bottom: none; }
  .featured li svg { flex: none; }
  .general { left: 421px; top: 343px; width: 449px; height: 341px; background: var(--slate); }
  .general .art { position: absolute; left: 100px; top: 54px; width: 273px; height: 268px;
    background: linear-gradient(160deg, #f2b33d 0%, #e44c3c 45%, #1d6b8c 100%); border-radius: 4px; }
  .blog { left: 884px; top: 343px; width: 242px; height: 165px; background: var(--gold); }
  .news { left: 884px; top: 519px; width: 242px; height: 165px; background: var(--blue); padding: 22px 19px; }
  .news-head { display: flex; justify-content: space-between; align-items: center; font-size: 16px; font-weight: 700; }
  .news time { display: block; margin-top: 22px; font-size: 13px; font-weight: 700; }
  .news p { margin-top: 8px; font-size: 13px; line-height: 20px; }
  .news a { display: block; margin-top: 10px; font-size: 11px; font-weight: 700; color: var(--white); text-decoration: none; }
  .footer { position: absolute; top: 704px; width: 100%; text-align: center; font-size: 11px; color: var(--muted); }
</style>
</head>
<body>
  <div class="backdrop" role="img" aria-label="Purple-tinted photograph of a capitol building"></div>

  <div class="brand">FUND LANTERN</div>
  <ul class="social">
    <li>Kinra</li><li>Swiftly</li><li>Plexa</li><li>Lumo</li><li>Worklink</li><li>Vidora</li>
  </ul>

  <nav class="nav">
    <a class="active" style="left:75px;width:89px">HOME</a>
    <a style="left:174px;width:89px">ABOUT</a>
    <a style="left:272px;width:178px">FEATURED ELECTIONS</a>
    <a style="left:458px;width:89px">BLOG</a>
    <a style="left:556px;width:144px">NEWS &amp; EVENTS</a>
    <a style="left:709px;width:89px">CONTACT</a>
  </nav>
  <div class="site-search">
    <span>Search...</span>
    <svg width="14" height="14" viewBox="0 0 14 14"><circle cx="6" cy="6" r="4.5" fill="none" stroke="#fff" stroke-width="2"/><line x1="9.3" y1="9.3" x2="13" y2="13" stroke="#fff" stroke-width="2"/></svg>
  </div>

  <div class="tile photo" role="img" aria-label="Photograph of ballots sorted into labelled trays"></div>

  <section class="tile about">
    <div class="icon-slot" role="img" aria-label="Group of people icon"></div>
    <div class="tile-title" style="left:19px;bottom:22px">ABOUT US</div>
  </section>

  <section class="tile services">
    <svg style="position:absolute;left:23px;top:24px" width="86" height="76" viewBox="0 0 86 76">
      <path d="M28 14 V6 a4 4 0 0 1 4 -4 h22 a4 4 0 0 1 4 4 v8" fill="none" stroke="#fff" stroke-width="6"/>
      <rect x="0" y="14" width="13" height="62" rx="5" fill="#fff"/>
      <rect x="18" y="14" width="50" height="62" fill="#fff"/>
      <rect x="73" y="14" width="13" height="62" rx="5" fill="#fff"/>
    </svg>
    <div class="tile-title" style="left:22px;bottom:22px">SERVICES</div>
  </section>

  <section class="tile election-search">
    <h2>ELECTION SEARCH</h2>
    <div class="select"><span>Select Election year</span><span>&#8597;</span></div>
    <div class="select"><span>Search candidate type</span><span>&#8597;</span></div>
    <div class="search-btn">SEARCH</div>
  </section>

  <section class="tile featured">
    <h2>FEATURED ELECTIONS</h2>
    <ul>
      <li><svg width="14" height="11" viewBox="0 0 14 11"><path d="M1 6 l4 4 l8 -9" fill="none" stroke="#fff" stroke-width="2.4"/></svg>2016 Election Night Results</li>
      <li><svg width="14" height="11" viewBox="0 0 14 11"><path d="M1 6 l4 4 l8 -9" fill="none" stroke="#fff" stroke-width="2.4"/></svg>Elections Calendar &amp; Upcoming Events</li>
      <li><svg width="14" height="11" viewBox="0 0 14 11"><path d="M1 6 l4 4 l8 -9" fill="none" stroke="#fff" stroke-width="2.4"/></svg>Voting In This Election</li>
      <li><svg width="14" height="11" viewBox="0 0 14 11"><path d="M1 6 l4 4 l8 -9" fill="none" stroke="#fff" stroke-width="2.4"/></svg>Campaign Finance &amp; Reporting</li>
      <li><svg width="14" height="11" viewBox="0 0 14 11"><path d="M1 6 l4 4 l8 -9" fill="none" stroke="#fff" stroke-width="2.4"/></svg>Running for Office</li>
      <li><svg width="14" height="11" viewBox="0 0 14 11"><path d="M1 6 l4 4 l8 -9" fill="none" stroke="#fff" stroke-width="2.4"/></svg>Voter Registration &amp; Historical Election Data</li>
      <li><svg width="14" height="11" viewBox="0 0 14 11"><path d="M1 6 l4 4 l8 -9" fill="none" stroke="#fff" stroke-width="2.4"/></svg>Velmor Election Laws &amp; Publications</li>
    </ul>
  </section>

  <section class="tile general">
    <div class="tile-title" style="left:34px;top:22px">GENERAL INFORMATION</div>
    <div class="art" role="img" aria-label="Illustration of election day with candidates, a calendar and a results chart"></div>
  </section>

  <section class="tile blog">
    <svg style="position:absolute;left:20px;top:16px" width="78" height="78" viewBox="0 0 78 78">
      <circle cx="11" cy="67" r="10" fill="#fff"/>
      <path d="M2 38 a38 38 0 0 1 38 38" fill="none" stroke="#fff" stroke-width="11"/>
      <path d="M2 10 a66 66 0 0 1 66 66" fill="none" stroke="#fff" stroke-width="11"/>
    </svg>
    <div class="tile-title" style="left:20px;bottom:10px">RECENT BLOG POST</div>
  </section>

  <section class="tile news">
    <div class="news-head"><span>NEWS &amp; EVENTS</span><span style="font-size:18px">&lsaquo; &rsaquo;</span></div>
    <time>MAY 16, 2017</time>
    <p>Nemo enim ipsam voluptatem voluptas sit aspernatur..</p>
    <a href="#">Read More</a>
  </section>

  <footer class="footer">Copyright © 2017. Company Name. All Right Reserved</footer>
</body>
</html>
```